A new presentation to our clients

we are a Real Estate agency, our website is www.dorelumia.com and it’s time to have a new, fashion and remarcable Business Card. we want to differentiate ourselves from other companies so we want a business card that differentiates us. we want the business card to impact our customers. in the competitive market that we have today, we have to be different and it is this difference that we seek

Target Market(s)

Real Estate Clients

Contact Information for Business Card

We search a totaly diferent card from the usual

Font styles to use
Sans Serif

Colors
e34197

Requirements
Must have
• Logo, adress, phone contact, e-mail, photo, and our website
Nice to have
• We would like to see a modern business card
Should not have
• Houses or building draws

```html
<!DOCTYPE html>
<html lang="en">
<head>
<meta charset="utf-8">
<title>Dore Lumia – Business Card</title>
<link rel="stylesheet" href="https://fonts.googleapis.com/css2?family=Comfortaa:wght@600&family=Montserrat:wght@400;600;700&family=Roboto:wght@400;500&display=swap">
<style>
  :root{
    --pink:#e34197;
    --pink-deep:#c81f6f;
    --ink:#1f1d1e;
    --ink-soft:#2b2829;
    --paper:#ffffff;
    --mist:#e9e9ea;
    --stage:#2c2c2d;
    --grey-text:#cfcfcf;
  }
  *{box-sizing:border-box;margin:0;padding:0}
  html,body{width:1200px;height:997px;overflow:hidden;background:var(--stage)}
  body{position:relative;font-family:"Roboto",Arial,sans-serif}

  .card{position:absolute;border-radius:4px;overflow:hidden;box-shadow:0 18px 40px rgba(0,0,0,.45)}

  /* Front */
  .card-front{left:70px;top:150px;width:540px;height:300px;background:var(--ink)}
  .front-top{position:absolute;left:0;top:0;width:100%;height:148px;background:linear-gradient(180deg,#fff 0%,#f1f1f1 100%)}
  .front-rule{position:absolute;left:0;top:148px;width:100%;height:5px;background:var(--pink)}
  .front-logo{position:absolute;left:0;right:0;top:46px;text-align:center;font-family:"Comfortaa",sans-serif;font-weight:600;font-size:64px;color:var(--pink);letter-spacing:1px}
  .front-address{position:absolute;right:22px;top:168px;text-align:right;color:var(--grey-text);font-size:12px;line-height:16px}
  .person{position:absolute;left:22px;top:170px}
  .person-name{color:var(--pink);font-weight:500;font-size:13px;letter-spacing:.5px;position:relative}
  .person-name::before{content:"";position:absolute;left:-2px;top:-12px;border-left:7px solid transparent;border-right:7px solid transparent;border-top:8px solid var(--pink)}
  .person-role{color:var(--grey-text);font-size:12px;margin-top:2px}
  .contacts{list-style:none;margin-top:12px}
  .contacts li{display:flex;align-items:center;gap:10px;color:var(--grey-text);font-size:12px;height:18px}
  .contacts svg{width:13px;height:13px;flex:none}
  .front-web{position:absolute;left:0;bottom:0;width:100%;height:32px;background:var(--pink);display:flex;align-items:center;justify-content:flex-end;padding-right:120px;color:#fff;font-size:13px;font-weight:500;letter-spacing:2px}

  /* Back */
  .card-back{left:570px;top:470px;width:560px;height:320px}
  .back-photo{position:absolute;inset:0;background:linear-gradient(160deg,#d9d9d9 0%,#b9b9ba 35%,#8d8c8d 60%,#c9c9c9 100%)}
  .back-veil{position:absolute;inset:0;background:rgba(255,255,255,.35)}
  .back-logo{position:absolute;left:0;right:0;top:66px;text-align:center;font-family:"Comfortaa",sans-serif;font-weight:600;font-size:62px;color:var(--pink);letter-spacing:1px}
  .tagline{position:absolute;left:70px;top:150px;font-family:"Montserrat",sans-serif;font-weight:700;font-size:23px;color:#fff;text-shadow:0 1px 3px rgba(0,0,0,.35)}
  .tagline-sub{position:absolute;left:240px;top:180px;font-size:8px;color:#fff}
  .search-btn{position:absolute;right:40px;top:172px;width:104px;height:22px;background:var(--pink);color:#fff;font-size:7px;font-family:"Montserrat",sans-serif;font-weight:600;display:flex;align-items:center;justify-content:center;gap:5px}
  .search-ref{position:absolute;right:44px;top:198px;font-size:7px;color:#fff}
  .search-form{position:absolute;left:70px;top:214px;width:306px;height:26px;background:#fff;display:flex}
  .field{flex:1;padding:3px 8px;border-right:1px solid var(--mist);font-size:7px;line-height:9px}
  .field:last-child{flex:1.5;border-right:0}
  .field-label{color:var(--pink);font-weight:500}
  .field-value{color:#666}
</style>
</head>
<body>

<section class="card card-front" aria-label="Business card front">
  <div class="front-top"></div>
  <div class="front-rule"></div>
  <div class="front-logo">Dore Lumia</div>
  <address class="front-address" style="font-style:normal">412 North Bay Street - Linden<br>New Jersey 07036</address>
  <div class="person">
    <div class="person-name">MARCO L. FERREIRA</div>
    <div class="person-role">Director &amp; Business Adviser</div>
    <ul class="contacts">
      <li><svg viewBox="0 0 14 14"><circle cx="7" cy="7" r="7" fill="#e34197"/><path d="M4.5 4h2l.6 1.6-1 .7a4.5 4.5 0 0 0 1.6 1.6l.7-1 1.6.6v2c-3.5 0-5.5-2-5.5-5.5z" fill="#fff"/></svg>555-014-2281</li>
      <li><svg viewBox="0 0 14 14"><circle cx="7" cy="7" r="7" fill="#e34197"/><rect x="5" y="3.5" width="4" height="7" rx=".8" fill="#fff"/></svg>555-018-7730</li>
      <li><svg viewBox="0 0 14 14"><circle cx="7" cy="7" r="7" fill="#e34197"/><rect x="3.5" y="4.5" width="7" height="5" fill="#fff"/><path d="M3.5 4.5 7 7.3l3.5-2.8" stroke="#e34197" stroke-width=".8" fill="none"/></svg>marco@mailbox.com</li>
    </ul>
  </div>
  <div class="front-web">www.dorelumia.com</div>
</section>

<section class="card card-back" aria-label="Business card back">
  <div class="back-photo" role="img" aria-label="Photo of a bright modern living room with a grey sofa, framed pictures and a large window"></div>
  <div class="back-veil"></div>
  <div class="back-logo">Dore Lumia</div>
  <div class="tagline">THE HOUSE OF YOUR DREAMS!</div>
  <div class="tagline-sub">Real Estate Agencies</div>
  <div class="search-btn"><svg width="7" height="7" viewBox="0 0 10 10"><circle cx="4" cy="4" r="3" stroke="#fff" stroke-width="1.5" fill="none"/><path d="M6.3 6.3 9 9" stroke="#fff" stroke-width="1.5"/></svg>SEARCH FOR</div>
  <div class="search-ref">... search by reference</div>
  <div class="search-form">
    <div class="field"><div class="field-label">Goal</div><div class="field-value">Select</div></div>
    <div class="field"><div class="field-label">Property Type</div><div class="field-value">Select</div></div>
    <div class="field"><div class="field-label">First Name</div><div class="field-value">Type a city or area</div></div>
  </div>
</section>

</body>
</html>
```